Business Card Design and Logo Needed

I need Business Cards and a Logo for my website and public speaking business which can be found at: www.kelsa-thorn.example

I'm looking for creative and unique ideas. Some business cards I've found online that I like can be found at:
http://gigplatelo.example/general/18-smokin-hot-business-card-designs/

and at

http://www.vortaplume.example/2009/04/50-creative-business-cards-of-50-graphic-designers/

```html
<!DOCTYPE html>
<html lang="en">
<head>
<meta charset="utf-8">
<title>Kelsa Thorn — Business Card</title>
<link rel="stylesheet" href="https://fonts.googleapis.com/css2?family=Marcellus&family=Cinzel:wght@400;700&display=swap">
<style>
  :root {
    --wood-dark: #4a2412;
    --glow: #f08a1e;
    --paper: #dcd6cc;
    --paper-edge: #f3efe8;
    --portrait-tone: #e6cfa6;
    --ink-engraved: #2e1608;
    --ink-name: #3b3835;
    --ink-contact: #b9a998;
    --ink-contact-label: #9c8d80;
  }
  html, body {
    margin: 0;
    padding: 0;
    width: 1200px;
    height: 640px;
    overflow: hidden;
    background: var(--wood-dark);
  }
  .card {
    position: relative;
    width: 1200px;
    height: 640px;
    overflow: hidden;
  }
  .card__art {
    position: absolute;
    inset: 0;
  }
  .roles {
    position: absolute;
    left: 566px;
    top: -4px;
    margin: 0;
    padding: 0;
    list-style: none;
    font-family: "Marcellus", serif;
    font-size: 51px;
    line-height: 70px;
    color: var(--ink-engraved);
    white-space: nowrap;
    text-shadow: 0 1px 0 rgba(255, 190, 130, 0.35), 0 -1px 1px rgba(0, 0, 0, 0.5);
  }
  .roles li:nth-child(3) { margin-top: 8px; }
  .name {
    position: absolute;
    left: 120px;
    top: 414px;
    margin: 0;
    font-family: "Marcellus", sans-serif;
    font-weight: 400;
    font-size: 52px;
    line-height: 1;
    letter-spacing: 3px;
    color: var(--ink-name);
    white-space: nowrap;
    transform-origin: 0 0;
    transform: rotate(21deg);
    text-shadow: 1px 2px 2px rgba(0, 0, 0, 0.35);
  }
  .contact {
    position: absolute;
    left: 870px;
    top: 480px;
    margin: 0;
    font-family: "Cinzel", serif;
    font-weight: 700;
    font-size: 22px;
    line-height: 38px;
    color: var(--ink-contact);
    white-space: nowrap;
    text-shadow: 0 1px 1px rgba(0, 0, 0, 0.45);
  }
  .contact__label {
    display: block;
    text-transform: uppercase;
    line-height: 28px;
    color: var(--ink-contact-label);
  }
</style>
</head>
<body>
<main class="card">
  <svg class="card__art" width="1200" height="640" viewBox="0 0 1200 640" xmlns="http://www.w3.org/2000/svg">
    <defs>
      <linearGradient id="wood-tone" x1="0" y1="0" x2="1" y2="1">
        <stop offset="0" stop-color="#a35a2a"/>
        <stop offset="0.45" stop-color="#7e4020"/>
        <stop offset="1" stop-color="#5a2a14"/>
      </linearGradient>
      <radialGradient id="tear-glow" cx="400" cy="260" r="420" gradientUnits="userSpaceOnUse">
        <stop offset="0" stop-color="#ffb347" stop-opacity="0.95"/>
        <stop offset="0.35" stop-color="#f08a1e" stop-opacity="0.7"/>
        <stop offset="1" stop-color="#f08a1e" stop-opacity="0"/>
      </radialGradient>
      <radialGradient id="corner-glow" cx="60" cy="600" r="260" gradientUnits="userSpaceOnUse">
        <stop offset="0" stop-color="#f5a040" stop-opacity="0.8"/>
        <stop offset="1" stop-color="#f08a1e" stop-opacity="0"/>
      </radialGradient>
      <linearGradient id="paper-tone" x1="0" y1="0" x2="1" y2="1">
        <stop offset="0" stop-color="#e2ded8"/>
        <stop offset="1" stop-color="#cfc9c0"/>
      </linearGradient>
      <filter id="paper-shadow" x="-10%" y="-10%" width="130%" height="130%">
        <feDropShadow dx="3" dy="4" stdDeviation="4" flood-color="#000" flood-opacity="0.45"/>
      </filter>
    </defs>

    <rect class="wood-panel" role="img" aria-label="Weathered wooden planks background" width="1200" height="640" fill="url(#wood-tone)"/>
    <rect class="wood-glow" width="1200" height="640" fill="url(#tear-glow)"/>
    <rect class="wood-glow" width="1200" height="640" fill="url(#corner-glow)"/>

    <polygon class="paper-corner" filter="url(#paper-shadow)" fill="url(#paper-tone)" stroke="var(--paper-edge)" stroke-width="2"
      points="0,0 502,0 491,23 463,30 458,58 429,65 424,94 396,101 391,129 362,136 357,164 329,171 324,200 295,207 290,235 262,242 257,270 229,277 223,306 195,313 190,341 162,348 156,376 128,383 123,412 95,419 90,447 61,454 56,482 28,489 23,518 0,530"/>

    <rect class="portrait" role="img" aria-label="Pale portrait silhouette of the speaker in profile" x="48" y="32" width="190" height="290" rx="90" fill="var(--portrait-tone)" opacity="0.55"/>

    <polygon class="name-strip" filter="url(#paper-shadow)" fill="var(--paper)" stroke="var(--paper-edge)" stroke-width="2"
      points="107,390 140,396 170,412 205,414 240,430 272,432 305,448 340,451 372,466 408,469 440,485 475,488 508,504 542,507 575,523 610,526 642,542 676,545 708,562 730,580 745,605 752,640 430,640 0,528 0,518 18,505 28,490 42,480 52,462 66,452 74,432 88,422 96,402"/>
  </svg>

  <ul class="roles">
    <li>Speaker</li>
    <li>Philantropist</li>
    <li>Author of Upcoming Book</li>
  </ul>

  <h1 class="name">KELSA THORN</h1>

  <p class="contact">
    <span class="contact__label">Contact Info:</span>
    BLah BLah BLah at Blah<br>
    BLah Street, Blah Avenue,<br>
    Blah Blah
  </p>
</main>
</body>
</html>
```